Venue Booking Site

I would like a venue directory and booking website designed. The idea is that end users will come to the site to find venues for weddings, parties, events etc. They will be able to find the venue based on many criteria, the most important ones are availability and location - they will be able to see in real time which venues are available for the desired dates and areas.

Venues will be able to use the website as a reservation management tool, receive payments for bookings through the site and be able to manage bookings on the go. This will be made into an app. It needs to be developed in bootstrap. Brand name to be used: Mirqona. Venue, place and space bookings.

Target audience - end users - anyone who is looking for a venue. For Community members it will provide an easy way to find a suitable venue
Outline what dates and times the venue is available
Outline costs involved in booking the venue
Search via many other criteria
It will allow the customer to book and pay for the venue online in one smooth process

Clients: Venue managers - particularly focussing on not for profit businesses eg, GHAs, community hall managers, small business managers. These people typically use paper based systems yet and do not use websites so it needs to be very user friendly. Future growth to restaurants, pubs, event venues who have a stronger familiarity with computers and who might already use their own booking management tool - so this needs to be able to link in with their system.

What need will this meet for venue managers:
This tool provides venues with greater visibility, promotion and advertising of their venue
This allows more customers to find them and book with them
This tool will be offered to not-for-profit venue managers for free to better connect them to the community
This means greater profit for these community venues
This means more revenue and jobs created in these communities

Sample of the layout / contents attached. This is not a complete site map as yet as it is a work in progress for final pages.

Small Business

5+ page

Sans Serif

eb2027

• This is a psd file only - one template for each different section, home page, search page, detailed page view, admin back end
• does not need to be coded.
• Note, the golden lantern logo jpeg files were files we were toying with using for this project- but I am happy to use the main mirqona logo- I will let you decide.

```html
<!DOCTYPE html>
<html lang="en">
<head>
<meta charset="utf-8">
<title>Mirqona – Venue Admin</title>
<link rel="stylesheet" href="https://fonts.googleapis.com/css2?family=Arimo:wght@400;700&display=swap">
<style>
:root{
  --brand:#eb2027;
  --brand-soft:#f2525a;
  --topbar:#2b2b2b;
  --ink:#111;
  --muted:#9a9a9a;
  --rule:#f4b5b8;
  --panel:#e8e8e8;
  --nav:#efefef;
  --pill:#a3a3a3;
  --footer:#000;
  --white:#fff;
}
*{box-sizing:border-box;margin:0;padding:0}
html,body{width:823px;height:1200px;overflow:hidden;background:var(--white)}
body{position:relative;font-family:"Arimo",Arial,sans-serif;color:var(--ink)}
.abs{position:absolute}

.topbar{left:0;top:0;width:823px;height:35px;background:var(--topbar);color:#ddd;font-size:10px}
.topbar .contact{top:13px;display:flex;align-items:center;gap:8px}
.topbar .divider{left:163px;top:11px;width:1px;height:14px;background:#555}
.topbar .social{right:45px;top:11px;display:flex;gap:5px}
.topbar .social span{width:15px;height:15px;border-radius:50%;background:#5a5a5a}

.brand{left:60px;top:44px;display:flex;align-items:center;gap:7px;color:var(--brand);font-weight:700;font-size:26px;letter-spacing:-.5px}
.brand i{width:14px;height:14px;background:var(--brand)}
.pill{top:54px;height:20px;border-radius:4px;background:var(--pill);color:#f3f3f3;font-size:6.5px;display:flex;align-items:center;padding:0 10px;justify-content:space-between}
.search{left:571px;width:213px}

.nav{left:4px;top:96px;width:819px;height:35px;background:var(--nav);border-bottom:3px solid #bdb8b3;display:flex;font-size:11px;font-weight:700}
.nav a{color:var(--ink);text-decoration:none;display:flex;align-items:center;justify-content:center;border-right:1px solid #d6d6d6}
.nav a.active{color:var(--brand)}

.sidemenu{left:49px;top:175px;width:157px;height:363px;background:var(--panel)}
.sidemenu .item{position:absolute;left:0;width:157px;display:flex;align-items:center;font-size:10.5px;font-weight:700;line-height:1.1}
.sidemenu .item svg{position:absolute;left:14px}
.sidemenu .item span{position:absolute;left:59px}
.sidemenu .item.active{top:0;height:69px;background:var(--brand-soft);color:var(--white)}
.sidemenu .item.active::after{content:"";position:absolute;right:-9px;top:28px;border-left:9px solid var(--brand-soft);border-top:7px solid transparent;border-bottom:7px solid transparent}

.section-title{left:275px;font-size:13px;font-weight:700}
.section-icon{left:243px}
.note{font-size:8.5px;color:#222}
.field{height:16px;border-bottom:1px solid var(--rule);font-size:9px;color:var(--muted);line-height:10px}
.full{left:288px;width:474px}
.label{font-size:9px;color:var(--muted)}
.check{display:flex;align-items:center;gap:8px;font-size:9px;color:#222}
.check i{width:8px;height:6px;background:var(--brand-soft)}

.footer{left:0;top:1000px;width:823px;height:200px;background:var(--footer);color:var(--white)}
.footer .social span{position:absolute;top:12px;width:34px;height:34px;border-radius:50%;background:var(--white)}
.footer .wordmark{left:56px;top:84px;font-size:32px;color:#9e9e9e;font-weight:700;letter-spacing:-.5px}
.footer h4{font-size:10px;font-weight:400;letter-spacing:.2px}
.footer .col p{font-size:10px;line-height:15.5px}
.footer .email-in{left:558px;top:100px;width:194px;height:22px;border-radius:11px;background:var(--white);color:#aaa;font-size:7px;display:flex;align-items:center;justify-content:center}
.footer .cta{left:624px;top:134px;width:63px;height:20px;background:var(--brand-soft);font-size:7.5px;display:flex;align-items:center;justify-content:center}
</style>
</head>
<body>

<header>
  <div class="abs topbar">
    <div class="abs contact" style="left:67px">
      <svg width="12" height="12" viewBox="0 0 12 12"><path d="M2 1l2 0 1 3-1.5 1a6 6 0 003 3L8 6.5l3 1v2c0 1-1 1.5-2 1.5A9 9 0 011 3c0-1 .5-2 1-2z" fill="var(--brand)"/></svg>
      <span>03 5521 4076</span>
    </div>
    <div class="abs divider"></div>
    <div class="abs contact" style="left:179px">
      <svg width="12" height="9" viewBox="0 0 12 9"><rect x=".5" y=".5" width="11" height="8" fill="none" stroke="var(--brand)"/><path d="M.5 .5L6 5l5.5-4.5" fill="none" stroke="var(--brand)"/></svg>
      <span>hello@venuedesk.example.au</span>
    </div>
    <div class="abs social"><span></span><span></span><span></span><span></span><span></span><span></span><span></span><span></span></div>
  </div>

  <div class="abs brand"><i></i>mirqona</div>
  <div class="abs pill" style="left:424px;width:66px">SIGN IN <span>●</span></div>
  <div class="abs pill" style="left:494px;width:65px">SIGN UP <span>●</span></div>
  <div class="abs pill search">SEARCH <span>⚲</span></div>

  <nav class="abs nav">
    <a class="active" href="#" style="width:127px">HOME</a>
    <a href="#" style="width:111px">VENUES</a>
    <a href="#" style="width:160px">NEWS &amp; OFFERS</a>
    <a href="#" style="width:144px">INSPIRATION</a>
    <a href="#" style="width:129px">SERVICES</a>
    <a href="#" style="width:108px;border-right:0">CONTACT</a>
  </nav>
</header>

<aside class="abs sidemenu">
  <div class="item active">
    <svg width="30" height="30" viewBox="0 0 30 30" style="top:20px"><circle cx="15" cy="9" r="6" fill="#fff"/><path d="M4 29c0-8 5-12 11-12s11 4 11 12z" fill="#fff"/><path d="M15 18l-1.5 4 1.5 6 1.5-6z" fill="var(--brand)"/></svg>
    <span>Admin</span>
  </div>
  <div class="item" style="top:84px;height:30px">
    <svg width="32" height="26" viewBox="0 0 32 26"><path d="M16 1L1 13h4v12h22V13h4z" fill="#000"/></svg>
    <span>Venue</span>
  </div>
  <div class="item" style="top:140px;height:30px">
    <svg width="38" height="24" viewBox="0 0 38 24"><rect x="0" y="2" width="3" height="21" fill="#000"/><rect x="0" y="16" width="38" height="3" fill="#000"/><rect x="35" y="10" width="3" height="13" fill="#000"/><circle cx="8" cy="11" r="3.5" fill="#000"/><rect x="13" y="9" width="22" height="6" fill="#000"/></svg>
    <span>Rooms/<br>Resources</span>
  </div>
  <div class="item" style="top:200px;height:32px">
    <svg width="32" height="32" viewBox="0 0 32 32"><rect x="1" y="4" width="30" height="27" rx="3" fill="#000"/><rect x="7" y="0" width="3" height="7" fill="#000"/><rect x="22" y="0" width="3" height="7" fill="#000"/><g fill="#fff"><rect x="5" y="12" width="5" height="4"/><rect x="13" y="12" width="5" height="4"/><rect x="21" y="12" width="5" height="4"/><rect x="5" y="20" width="5" height="4"/><rect x="13" y="20" width="5" height="4"/><rect x="21" y="20" width="5" height="4"/></g></svg>
    <span>Calendar</span>
  </div>
  <div class="item" style="top:259px;height:32px">
    <svg width="32" height="30" viewBox="0 0 32 30"><path d="M1 17l4-3 7 8L29 1l2 2-18 26z" fill="#000"/></svg>
    <span>Bookings</span>
  </div>
  <div class="item" style="top:318px;height:32px">
    <svg width="32" height="30" viewBox="0 0 32 30"><rect x="1.5" y="4.5" width="22" height="24" fill="none" stroke="#000" stroke-width="2"/><path d="M5 11h12M5 16h12M5 21h12" stroke="#000" stroke-width="2"/><path d="M18 20L30 3l2 2-12 17-3 1z" fill="#000"/></svg>
    <span>Reports</span>
  </div>
</aside>

<main>
  <svg class="abs section-icon" style="top:178px" width="22" height="28" viewBox="0 0 22 28"><path d="M11 1a9 9 0 00-4 17v9l4 0 0-9a9 9 0 00-0-17zm0 4a5 5 0 110 10 5 5 0 010-10z" fill="#000"/></svg>
  <h2 class="abs section-title" style="top:181px">Venue contact</h2>
  <div class="abs field full" style="top:212px">Venue E-mail:</div>
  <div class="abs field full" style="top:245px">Venue Phone number:</div>

  <svg class="abs section-icon" style="top:303px" width="26" height="26" viewBox="0 0 26 26"><rect x="4" y="1" width="20" height="14" rx="2" fill="#000" transform="rotate(-8 14 8)"/><rect x="1.5" y="8.5" width="22" height="15" rx="2" fill="#fff" stroke="#000" stroke-width="2"/><rect x="2" y="12" width="21" height="3" fill="#000"/></svg>
  <h2 class="abs section-title" style="top:308px">Banking Details</h2>
  <p class="abs note" style="left:288px;top:329px">These details will be used to allow customers to pay booking fees into your bank account.</p>
  <div class="abs field full" style="top:357px">Acccount name:</div>
  <div class="abs field" style="left:288px;top:389px;width:176px">BSB:</div>
  <div class="abs field" style="left:468px;top:389px;width:294px">Account Number:</div>

  <svg class="abs section-icon" style="top:446px" width="22" height="26" viewBox="0 0 22 26"><circle cx="11" cy="6" r="5.5" fill="#000"/><path d="M1 25c0-8 4-12 10-12s10 4 10 12z" fill="#000"/></svg>
  <h2 class="abs section-title" style="top:448px">Venue Mannager’s details</h2>
  <p class="abs note" style="left:286px;top:471px">These details will be used to notify you of new bookings and will not be visible to customers</p>
  <div class="abs field full" style="top:489px">Manager’s mobile:</div>
  <div class="abs field full" style="top:518px">Manager’s email:</div>
  <p class="abs label" style="left:288px;top:545px">How do you want to be notified of new bookins:</p>
  <div class="abs check" style="left:293px;top:572px"><i></i>SMS</div>
  <div class="abs check" style="left:504px;top:572px"><i></i>Email</div>
  <div class="abs check" style="left:290px;top:596px;font-size:10px">
    <svg width="14" height="14" viewBox="0 0 14 14"><circle cx="7" cy="7" r="6" fill="none" stroke="var(--brand)"/><path d="M7 4v6M4 7h6" stroke="var(--brand)"/></svg>
    Add another venue manager’s details
  </div>

  <svg class="abs section-icon" style="top:649px" width="22" height="26" viewBox="0 0 22 26"><path d="M1 1h13l7 7v17H1z" fill="#000"/><path d="M5 11h12M5 15h12M5 19h12" stroke="#fff" stroke-width="1.6"/></svg>
  <h2 class="abs section-title" style="top:656px">Venue Admin details</h2>
  <div class="abs field full" style="top:682px">Privacy policy (enter details)</div>
  <div class="abs field full" style="top:712px">Terms and conditions (every details)</div>
  <div class="abs field full" style="top:735px"></div>
  <div class="abs field full" style="top:758px"></div>
  <div class="abs field full" style="top:782px"></div>
  <div class="abs field full" style="top:806px"></div>
  <p class="abs label" style="left:288px;top:827px;line-height:11px">Public liability insurance<br>(Upload pdf or jpegs of convernote)</p>
  <svg class="abs" style="left:461px;top:835px" width="8" height="8" viewBox="0 0 8 8"><path d="M4 0L8 4H5.5v4h-3V4H0z" fill="var(--brand)"/></svg>
  <div class="abs field full" style="top:865px">ABN:</div>
  <div class="abs field full" style="top:891px">Bond per booking:</div>
  <div class="abs field full" style="top:919px">Non Refundable Deposit %:</div>
</main>

<footer class="abs footer">
  <div class="social">
    <span style="left:76px"></span><span style="left:161px"></span><span style="left:246px"></span><span style="left:331px"></span>
    <span style="left:416px"></span><span style="left:501px"></span><span style="left:587px"></span><span style="left:671px"></span>
  </div>
  <div class="abs wordmark">mirqona</div>
  <p class="abs" style="left:75px;top:152px;font-size:7.5px">© 2014 - PRIVACY POLICY</p>

  <div class="abs col" style="left:234px;top:78px">
    <h4>MIRQONA BOOKING</h4>
    <p style="margin-top:2px">12 Tallow Lane Ormond VIC<br>☎ 03 5521 4067<br>✉ hello@venuedesk.example.au</p>
  </div>
  <div class="abs col" style="left:391px;top:76px">
    <h4>CUSTOMER SUPPORT</h4>
    <p style="margin-top:2px;padding-left:2px">Faq<br>How do I make a reservation?<br>Payment options<br>Booking tips</p>
  </div>
  <h4 class="abs" style="left:566px;top:73px;font-weight:700">DON’T MISS OUR EXCLUSIVE OFFERS</h4>
  <div class="abs email-in">ENTER YOUR E-MAIL ID</div>
  <div class="abs cta">VIEW MORE</div>
</footer>

</body>
</html>
```